Let's help people Orlanta with better hearing!

I need a business card for my private practice. I am a Dr. of Audiology and focus on hearing and tinnitus (ringing in the ears) treatment. My practice is named "Orlanta Hearing and Tinnitus Solutions". I want to communicate the idea of improved quality of life utilizing a natural color pallet Love the color turquoise as an accent. Want a professional look, while eye catching. I'm open to nontraditional design aesthetic. Something to get excited about and motivate people to improve their lives!

```html
<!DOCTYPE html>
<html lang="en">
<head>
<meta charset="utf-8">
<title>Orlanta Hearing &amp; Tinnitus Solutions – Business Card</title>
<link rel="stylesheet" href="https://fonts.googleapis.com/css2?family=Josefin+Sans:wght@300&family=Open+Sans:wght@400&display=swap">
<style>
  :root {
    --turquoise: #5bc4c6;
    --card-white: #ffffff;
    --ink-grey: #7a7a7a;
    --ink-dark: #4a4a4a;
    --backdrop: #ecebe8;
    --font-display: "Josefin Sans", sans-serif;
    --font-body: "Open Sans", sans-serif;
  }
  * { box-sizing: border-box; margin: 0; padding: 0; }
  html, body {
    width: 1200px; height: 1000px; overflow: hidden;
    background: var(--backdrop);
  }
  .canvas {
    position: relative; width: 1200px; height: 1000px;
  }
  .card {
    position: absolute; left: 320px; width: 560px; height: 320px;
    box-shadow: 0 6px 18px rgba(0,0,0,0.12);
  }

  /* Front side */
  .card--front {
    top: 140px; background: var(--turquoise); color: var(--card-white);
    display: flex; flex-direction: column; align-items: center; justify-content: center;
  }
  .brand-name {
    font-family: var(--font-display); font-weight: 300;
    font-size: 78px; letter-spacing: 2px; line-height: 1;
    margin-bottom: 14px;
  }
  .tagline {
    width: 340px; border-top: 1.5px solid var(--card-white);
    border-bottom: 1.5px solid var(--card-white);
    padding: 14px 0 16px; text-align: center;
    font-family: var(--font-display); font-weight: 300;
    font-size: 24px; letter-spacing: 1px; line-height: 1.25;
    text-transform: uppercase;
  }

  /* Back side */
  .card--back { top: 540px; background: var(--card-white); }
  .holder {
    position: absolute; right: 28px; top: 26px; text-align: right;
    font-family: var(--font-body); color: var(--ink-grey);
  }
  .holder__name { font-size: 22px; letter-spacing: 0.5px; }
  .holder__role { font-size: 12px; margin-top: 2px; }
  .accent-rule {
    position: absolute; left: 28px; right: 0; top: 96px;
    height: 4px; background: var(--turquoise);
  }
  .contact-list {
    position: absolute; left: 300px; top: 120px; list-style: none;
    font-family: var(--font-body); font-size: 14px; color: var(--ink-dark);
  }
  .contact-list li {
    display: flex; align-items: center; gap: 10px; margin-bottom: 10px;
  }
  .contact-icon { width: 16px; height: 16px; flex: none; }
</style>
</head>
<body>
<main class="canvas">

  <section class="card card--front" aria-label="Card front">
    <h1 class="brand-name">Orlanta</h1>
    <p class="tagline">Hearing &amp; Tinnitus<br>Solutions</p>
  </section>

  <section class="card card--back" aria-label="Card back">
    <div class="holder">
      <p class="holder__name">Dr. Mara Ellison</p>
      <p class="holder__role">Audiologist</p>
    </div>
    <div class="accent-rule"></div>
    <ul class="contact-list">
      <li>
        <svg class="contact-icon" viewBox="0 0 16 16" aria-hidden="true">
          <path d="M4 1.5l2.2 3-1.3 1.4c.8 1.8 2.3 3.3 4.2 4.2l1.4-1.3 3 2.2-1.1 2.5C7.5 13.8 2.2 8.5 1.7 3.6z" fill="var(--ink-dark)"/>
        </svg>
        04 5512 3309
      </li>
      <li>
        <svg class="contact-icon" viewBox="0 0 16 16" aria-hidden="true">
          <circle cx="8" cy="8" r="6.5" fill="none" stroke="var(--ink-dark)" stroke-width="1.5"/>
        </svg>
        social.orlanta.com.au
      </li>
      <li>
        <svg class="contact-icon" viewBox="0 0 16 16" aria-hidden="true">
          <rect x="1.5" y="3.5" width="13" height="9" fill="none" stroke="var(--ink-dark)" stroke-width="1.3"/>
          <path d="M1.5 3.5L8 9l6.5-5.5" fill="none" stroke="var(--ink-dark)" stroke-width="1.3"/>
        </svg>
        info@orlanta.com.au
      </li>
      <li>
        <svg class="contact-icon" viewBox="0 0 16 16" aria-hidden="true">
          <rect x="1.5" y="2.5" width="13" height="9" fill="none" stroke="var(--ink-dark)" stroke-width="1.3"/>
          <path d="M5 14h6M8 11.5V14" stroke="var(--ink-dark)" stroke-width="1.3"/>
        </svg>
        www.orlanta.com.au
      </li>
    </ul>
  </section>

</main>
</body>
</html>
```